Business Card and Stationary for a nutrition health coaching company (Sunward Vitality)
Sunward Vitality
Simple
Marcus T. Holloway, Ph.D.
Holistic Health Counselor
Rua dos Pinheiros Altos 17
2715-093, Barcarena,
Portugal
marcus.holloway@sunward-vitality.example
www.sunward-vitality.example
The front side of the card should be in English - but the back side of the card should contain the same information but in Portuguese. Equivalent fields that I suspect will be labeled on the backside of the card are indicated below.
Holistic Health Counselor = Conselheiro de Saúde Holístico
Cell = Tlm.
Please use the logo below for the business card + stationary. Thank you!

```html
<!DOCTYPE html>
<html lang="en">
<head>
<meta charset="utf-8">
<title>Sunward Vitality — Stationery Set</title>
<link href="https://fonts.googleapis.com/css2?family=Raleway:wght@400;600&display=swap" rel="stylesheet">
<style>
  :root {
    --backdrop: #ece6dc;
    --paper: #ffffff;
    --paper-edge: #e2e2e2;
    --leaf-green: #6f9a2c;
    --leaf-green-dark: #4f7a1c;
    --leaf-green-light: #a8c66a;
    --mark-faint: #eef3e4;
    --ink: #5a5a5a;
    --ink-soft: #8a8a8a;
  }
  * { box-sizing: border-box; margin: 0; padding: 0; }
  html, body { width: 1200px; height: 600px; overflow: hidden; }
  body {
    background: var(--backdrop);
    font-family: "Raleway", sans-serif;
    color: var(--ink);
    position: relative;
  }
  .sheet {
    position: absolute;
    background: var(--paper);
    border: 1px solid var(--paper-edge);
    box-shadow: 0 2px 6px rgba(0,0,0,0.12);
    overflow: hidden;
  }
  .brand {
    display: flex; flex-direction: column; align-items: center; gap: 3px;
  }
  .brand-dot {
    width: 16px; height: 16px; border-radius: 50%; background: var(--leaf-green);
  }
  .brand-name {
    font-size: 11px; font-weight: 600; color: var(--leaf-green); letter-spacing: 0.5px;
  }
  .faint-mark {
    position: absolute; border-radius: 50%; background: var(--mark-faint);
  }

  /* Business card */
  .business-card { left: 19px; top: 238px; width: 132px; height: 120px; border-radius: 4px; }
  .business-card .brand { margin-top: 8px; }
  .card-band {
    position: absolute; left: 0; right: 0; top: 44px; height: 52px;
    background: linear-gradient(180deg, var(--leaf-green-light), var(--leaf-green));
    color: #fff; padding: 5px 8px; font-size: 5px; line-height: 1.45;
  }
  .card-band .person { font-size: 6.5px; font-weight: 600; }
  .card-footer { position: absolute; bottom: 6px; left: 0; right: 0; text-align: center; font-size: 4.5px; color: var(--ink-soft); }

  /* Letterhead */
  .letterhead { left: 283px; top: 19px; width: 300px; height: 490px; }
  .letterhead .brand { margin-top: 22px; }
  .letterhead .faint-mark { width: 120px; height: 120px; left: 90px; top: 175px; }
  .letterhead-band {
    position: absolute; left: 0; right: 0; bottom: 28px; height: 22px;
    background: linear-gradient(180deg, var(--leaf-green-light), var(--leaf-green-dark));
    display: flex; justify-content: space-around; align-items: center;
    color: #fff; font-size: 5px; padding: 0 10px;
  }

  /* Envelopes */
  .envelope-back { left: 653px; top: 132px; width: 487px; height: 132px; }
  .envelope-flap { position: absolute; inset: 0; }
  .envelope-back .brand { position: absolute; left: 50%; top: 30px; transform: translateX(-50%); }
  .envelope-web { position: absolute; left: 0; right: 0; top: 62px; text-align: center; font-size: 5px; letter-spacing: 1.5px; color: var(--ink-soft); }

  .envelope-front { left: 653px; top: 295px; width: 487px; height: 190px; }
  .envelope-front .brand { position: absolute; left: 22px; top: 22px; align-items: flex-start; }
  .return-address { position: absolute; left: 22px; top: 64px; font-size: 5px; line-height: 1.5; color: var(--ink-soft); }
  .envelope-front .faint-mark { width: 110px; height: 110px; right: 110px; top: 50px; }

  .caption {
    position: absolute; top: 528px; font-size: 7px; letter-spacing: 2px;
    text-transform: uppercase; color: var(--ink-soft);
  }
  .caption-letter { left: 283px; width: 300px; text-align: center; }
  .caption-envelope { left: 653px; width: 487px; text-align: center; }
</style>
</head>
<body>

  <section class="sheet business-card" aria-label="Business card">
    <div class="brand"><span class="brand-dot"></span><span class="brand-name">Sunward Vitality</span></div>
    <div class="card-band">
      <div class="person">Marcus T. Holloway, Ph.D.</div>
      <div>Holistic Health Counselor</div>
      <div>Rua dos Pinheiros Altos 17, 2715-093 Barcarena</div>
      <div>marcus.holloway@sunward-vitality.example</div>
    </div>
    <div class="card-footer">www.sunward-vitality.example</div>
  </section>

  <section class="sheet letterhead" aria-label="Letterhead">
    <div class="brand"><span class="brand-dot"></span><span class="brand-name">Sunward Vitality</span></div>
    <div class="faint-mark"></div>
    <div class="letterhead-band">
      <span>Rua dos Pinheiros Altos 17, 2715-093 Barcarena</span>
      <span>marcus.holloway@sunward-vitality.example</span>
      <span>www.sunward-vitality.example</span>
    </div>
  </section>

  <section class="sheet envelope-back" aria-label="Envelope back">
    <svg class="envelope-flap" viewBox="0 0 487 132" preserveAspectRatio="none" aria-hidden="true">
      <path d="M0 0 L40 70 Q243 95 447 70 L487 0" fill="none" stroke="#dcdcdc" stroke-width="1"/>
    </svg>
    <div class="brand"><span class="brand-dot"></span></div>
    <div class="envelope-web">WWW.SUNWARD-VITALITY.EXAMPLE</div>
  </section>

  <section class="sheet envelope-front" aria-label="Envelope front">
    <div class="brand"><span class="brand-dot"></span><span class="brand-name">Sunward Vitality</span></div>
    <div class="return-address">
      Rua dos Pinheiros Altos 17<br>2715-093, Barcarena<br>Portugal
    </div>
    <div class="faint-mark"></div>
  </section>

  <p class="caption caption-letter">Letter head Option 1</p>
  <p class="caption caption-envelope">Envelope Option 2</p>

</body>
</html>
```